Business card for apparel company. Specializing in fishing and boating performance wear. Main company name is Marlow Pelican Company, LLC brand name for apparel is TIDEWAKE. See website www.TidewakeBayline.com I will attach some logos to consider.

```html
<!DOCTYPE html>
<html lang="en">
<head>
<meta charset="utf-8">
<title>Tidewake Business Card</title>
<link href="https://fonts.googleapis.com/css2?family=Montserrat:wght@400;700;800&display=swap" rel="stylesheet">
<style>
  :root {
    --page: #ece8e1;
    --white: #ffffff;
    --ink: #262626;
    --band: #2f62ae;
    --brand: #2585d6;
    --back-light: #1f9ce0;
    --back-dark: #2c76c4;
  }
  * { margin: 0; padding: 0; box-sizing: border-box; }
  html, body { width: 900px; height: 1200px; overflow: hidden; }
  body {
    background: var(--page);
    font-family: "Montserrat", Arial, sans-serif;
    position: relative;
  }
  .card {
    position: absolute;
    left: 80px;
    width: 742px;
    height: 440px;
    border-radius: 30px;
    overflow: hidden;
  }
  .card-front { top: 132px; background: var(--white); }
  .card-back {
    top: 638px;
    background: linear-gradient(100deg, var(--back-light), var(--back-dark));
  }
  .header-band { position: absolute; inset: 0; }
  .holder { position: absolute; left: 50px; top: 60px; color: var(--white); }
  .holder-name { font-size: 26px; font-weight: 700; line-height: 1.2; }
  .holder-role { font-size: 16px; font-weight: 400; margin-top: 2px; }
  .address {
    position: absolute; left: 41px; top: 270px;
    font-size: 16.5px; line-height: 20px; color: var(--ink); font-style: normal;
  }
  .contacts {
    position: absolute; left: 43px; top: 350px;
    list-style: none; font-size: 16.5px; color: var(--ink); line-height: 22.5px;
  }
  .contacts li { display: flex; align-items: center; gap: 10px; }
  .contacts svg { width: 15px; height: 15px; fill: var(--brand); flex: none; }
  .brand-name { position: absolute; font-weight: 800; letter-spacing: 1px; }
  .brand-front {
    left: 388px; top: 268px; width: 320px; text-align: center;
    font-size: 46px; color: var(--brand);
  }
  .brand-back {
    left: 0; right: 0; top: 180px; text-align: center;
    font-size: 74px; color: var(--white);
  }
</style>
</head>
<body>
  <section class="card card-front">
    <svg class="header-band" viewBox="0 0 742 440" aria-hidden="true">
      <defs>
        <linearGradient id="headerBlue" x1="0" y1="0" x2="1" y2="0">
          <stop offset="0" stop-color="#55b2e8"/>
          <stop offset="1" stop-color="#2e5ca9"/>
        </linearGradient>
      </defs>
      <path d="M0,0 H742 V140 C560,120 420,170 300,195 C180,218 80,210 0,200 Z" fill="url(#headerBlue)"/>
      <path d="M0,210 C100,222 190,226 300,206 C420,184 560,136 742,150 V158 C560,146 420,196 300,216 C190,234 100,230 0,220 Z" fill="var(--band)"/>
    </svg>
    <div class="holder">
      <h1 class="holder-name">Callum Ashworth</h1>
      <p class="holder-role">Owner</p>
    </div>
    <address class="address">
      Marlow Pelican Company, LLC<br>
      P.O. Box 418<br>
      Seabright, Florida 34710
    </address>
    <ul class="contacts">
      <li><svg viewBox="0 0 16 16"><path d="M2 6c0-2 3-3 6-3s6 1 6 3v1h-3V6H5v1H2zM4 8h8l2 5H2z"/></svg>215-555-0147</li>
      <li><svg viewBox="0 0 16 16"><path d="M1 3h14v10H1zM2 4l6 5 6-5v1L8 10 2 5z" fill-rule="evenodd"/></svg>info@MarlowPelicanCo.com</li>
      <li><svg viewBox="0 0 16 16"><circle cx="8" cy="8" r="7"/></svg>www.TidewakeBayline.com</li>
    </ul>
    <p class="brand-name brand-front">TIDEWAKE</p>
  </section>

  <section class="card card-back">
    <p class="brand-name brand-back">TIDEWAKE</p>
  </section>
</body>
</html>
```